[AMAZING DESIGN NEEDED] Women's Fishing Squeeze Page

I need a professional design for a landing page that is going to collect email addresses.

You can use the creatives already on the page or you can pull images from the facebook/instagram pages.
https://www.facebook.com/LakesLuresBoots
https://www.instagram.com/lakesluresandboots/

This is the page that needs designed: https://lakesluresandboots.example/email-opt-in/

See attached for examples.

Target Market(s)

Women who like to go fishing

Industry/Entity Type

Fishing

Number of Pages Required

1 page

Font styles to use
Sans Serif

Requirements
Must have
• excellent design. Call to actions.

```html
<!DOCTYPE html>
<html lang="en">
<head>
<meta charset="utf-8">
<title>Lakes Lures and Boots – Sign Up</title>
<link rel="stylesheet" href="https://fonts.googleapis.com/css2?family=Roboto:wght@400;500;700&family=Titillium+Web:wght@400;600;700&display=swap">
<style>
  :root {
    --brown: #5a2d32;
    --white: #ffffff;
    --ink: #1f1f1f;
    --field-border: #d9d4d5;
    --field-text: #5b5b5b;
    --sky-teal: #1f7f9a;
    --dusk-dark: #2a2418;
  }
  * { box-sizing: border-box; margin: 0; padding: 0; }
  html, body { width: 1200px; height: 688px; overflow: hidden; background: var(--white); }
  .page { position: relative; width: 1200px; height: 688px; overflow: hidden; font-family: "Roboto", sans-serif; }

  .hero-photo {
    position: absolute; inset: 0;
    background:
      radial-gradient(ellipse 420px 300px at 430px 360px, rgba(240,190,40,.95), rgba(240,150,30,0) 70%),
      radial-gradient(ellipse 600px 260px at 500px 430px, rgba(220,80,30,.75), rgba(220,80,30,0) 70%),
      linear-gradient(100deg, #2f3a30 0%, #b07f1c 25%, #d79a1a 45%, #7a7a50 70%, var(--sky-teal) 100%);
  }
  .hero-photo::after {
    content: ""; position: absolute; left: 0; right: 0; bottom: 0; height: 260px;
    background: linear-gradient(to bottom, rgba(42,36,24,0), var(--dusk-dark));
  }

  .brand {
    position: absolute; left: 116px; top: 52px;
    display: flex; align-items: center; gap: 8px;
    font-family: "Titillium Web", sans-serif; font-weight: 600;
    font-size: 17px; line-height: 1.05; color: var(--white); text-decoration: none; width: 130px;
  }
  .brand-dot { width: 12px; height: 12px; border-radius: 50%; background: var(--white); flex: none; }

  .nav-top, .nav-main {
    position: absolute; right: 110px; display: flex; align-items: center;
    list-style: none; color: var(--white); font-size: 14.5px; letter-spacing: .3px;
  }
  .nav-top { top: 30px; gap: 26px; }
  .nav-main { top: 76px; gap: 30px; }
  .nav-top a, .nav-main a { color: var(--white); text-decoration: none; display: flex; align-items: center; gap: 5px; }
  .social-dots { display: flex; gap: 8px; margin-right: -8px; }
  .social-dots span { width: 11px; height: 11px; border-radius: 50%; border: 1.5px solid var(--white); display: block; }

  .signup-card {
    position: absolute; left: 727px; top: 195px; width: 336px; height: 360px;
    background: var(--brown); border-radius: 6px; padding: 8px;
  }
  .signup-inner {
    background: var(--white); border-radius: 6px; height: 343px; padding: 0 18px;
    display: flex; flex-direction: column; align-items: center;
  }
  .signup-title {
    font-family: "Titillium Web", sans-serif; font-weight: 600; font-size: 26px;
    color: var(--brown); margin-top: 38px; margin-bottom: 17px; letter-spacing: .3px;
  }
  .field {
    width: 285px; height: 43px; border: 1px solid var(--field-border); border-radius: 22px;
    padding: 0 15px; font-family: "Roboto", sans-serif; font-size: 14.5px; color: var(--field-text);
    margin-bottom: 8px; background: var(--white);
  }
  .field::placeholder { color: var(--field-text); }
  .subscribe-btn {
    width: 285px; height: 42px; margin-top: 8px; border: none; border-radius: 22px;
    background: var(--brown); color: var(--white); font-family: "Roboto", sans-serif;
    font-weight: 700; font-size: 14.5px; letter-spacing: .6px;
    box-shadow: 0 3px 6px rgba(0,0,0,.25);
  }

  .wave { position: absolute; left: 0; top: 0; width: 1200px; height: 688px; }
  .page-heading {
    position: absolute; left: 106px; top: 624px;
    font-family: "Titillium Web", sans-serif; font-weight: 700; font-size: 32px;
    letter-spacing: 1.4px; color: var(--ink);
  }
</style>
</head>
<body>
<div class="page">
  <div class="hero-photo" role="img" aria-label="Photo of an angler silhouetted against an orange sunset sky, casting a bent fishing rod over the water"></div>

  <a class="brand" href="https://lakesluresandboots.example"><span class="brand-dot"></span>Lakes Lures &amp; Boots</a>

  <ul class="nav-top">
    <li class="social-dots" aria-hidden="true"><span></span><span></span></li>
    <li><a href="#">SEARCH</a></li>
    <li><a href="#">GIFT</a></li>
    <li><a href="#">CERTIFICATES</a></li>
    <li><a href="#">
      <svg width="13" height="14" viewBox="0 0 13 14" fill="none" stroke="currentColor" stroke-width="1.4"><circle cx="6.5" cy="4" r="3"/><path d="M1 13.5c0-3 2.5-5 5.5-5s5.5 2 5.5 5z"/></svg>
      SIGN IN or REGISTER</a></li>
    <li><a href="#">
      <svg width="16" height="14" viewBox="0 0 16 14" fill="none" stroke="currentColor" stroke-width="1.3"><path d="M0.5 1h2.5l2 8h8l2-6H4"/><circle cx="6" cy="12" r="1.2"/><circle cx="12" cy="12" r="1.2"/></svg>
      CART</a></li>
  </ul>

  <ul class="nav-main">
    <li><a href="#">CLOTHING</a></li>
    <li><a href="#">HATS</a></li>
    <li><a href="#">BUNDLES</a></li>
    <li><a href="#">ACCESSORIES &amp; STICKERS</a></li>
    <li><a href="#">JEWELRY</a></li>
    <li><a href="#">CLEARANCE</a></li>
  </ul>

  <form class="signup-card" action="https://lakesluresandboots.example/email-opt-in/">
    <div class="signup-inner">
      <h2 class="signup-title">Sign Up Today</h2>
      <input class="field" type="text" placeholder="First Name">
      <input class="field" type="text" placeholder="Last Name">
      <input class="field" type="email" placeholder="Email Address">
      <button class="subscribe-btn" type="submit">SUBSCRIBE AND SAVE</button>
    </div>
  </form>

  <svg class="wave" viewBox="0 0 1200 688" aria-hidden="true">
    <path fill="#ffffff" d="M0 620 C120 570 260 552 400 566 C600 585 800 640 1000 660 C1100 665 1150 640 1200 615 L1200 688 L0 688 Z"/>
    <path fill="#5a2d32" d="M0 640 C150 588 280 578 420 592 C620 614 820 672 980 668 C1080 665 1150 640 1200 620 L1200 688 L900 688 C700 660 500 612 420 600 C280 584 150 594 0 643 Z"/>
  </svg>

  <h1 class="page-heading">LAKES LURES AND BOOTS</h1>
</div>
</body>
</html>
```